We need your help in designing the graphical look of the home page of our web site: Quellnest.com.

Quellnest is an FREE online service that brings consumers and service providers together through online reservations.

Our service is in fact a web application (similar to brindlo calendar), so we will be using forms, widgets, menus and standard web controls (buttons, fields, links, etc). We need a design that will be easy to integrate with our programming.

This design project is for the HOME page, but we will choose the designer that will design the web page in photoshop in layers, so we can easily derive our other secondary pages ourselves.

If you have any questions please send us a message and we will gladly update the brief with a response.

Happy Designing!
Updates

Hi all, the menu on the home page should be something standard, like: Pricing, features, how it works.

once a user is logged in, they will see their toolbox at all times:
- My Nest (links to their main page of bookings)
- My Faborites (view favorite businesses and book quickly with them)
- Settings (set parameters of their account)

There should be a My Profile page as well. 

Thanks!

Reason: I have extended the deadline to receive more designs.

Hi All,

UPDATE: we changed our vision of the home page to have a much simpler design.  something along the lines of tumbrella vexnor and mor tan.

HOME PAGE:
light colors with white background.  simple, simple, simple!

header should not be big, logo, change language link. try with search bar (what and where).

body should be simple, with an image + register form only.

footer with links to pages for more info:
- Privacy,
- Getting started
- How it works
- Contact us
- FAQ
- Pricing

LOGGED IN PAGE:
when logged in, the header can be the same or reduced to maximize the "working area" (body).
body can be a 2 or 3 column design, as we have a main working area.  in your design, show a calendar.  we need a toolbar (side or top) that will have these buttons, links: MyNest, My Favorites, Settings, My Profile.
We need a section that will display latest messages or notifications.
keep the footer with the links.

Thank you all.

Reason: Holidays

Reason: holidays... lets spend time with our families!

Target Market(s)

Young and mobile consumers + professionals, businesses, restaurants and commerces wishing to offer online reservations (appointments and reservations)

Industry/Entity Type

Brindlo

Requirements
Must have
• - Easy to integrate with web programming
- light weight visual design. We want something with light tone colors as background
- home page will have a content slider that will show some catch phrases.
- Overall design should be more on the "cartoony" side. Should give a casual, humour and friendly ambiance.

The home page should have these sections:
- a search section for consumers to find local businesses. They will search by specifying "What?" & "Where?"
- a content slider that will cycle through catch phrases and features. Each pane should have an image representative of the text.
- have 4 highlighted sections
- QuellNest is great for (list of different businesses types that use quelnest)
- QuellNest is available for FREE to everyone
- Main features list (accept 24/7 reservations, never reveal your schedule, automatic reminders, marketing campaigns)
- The more you quell, the more you save! (info on our loyalty program that entitles consumers to greater savings and benefits).

One a user logs in, all the certer page info will be replaced by a content div that will allow content to display based on selected menu item
- My Nest (opens the main section where all happens. This section should have a design that gives the impression that we're looking in a box)
- My Profile
- My Favorites
Should not have
• - Don't use actual photos of real people, rather opt for sketches and cartoony characters.

```html
<!DOCTYPE html>
<html lang="en">
<head>
<meta charset="utf-8">
<title>QuellNest – Home</title>
<link href="https://fonts.googleapis.com/css2?family=Ubuntu:wght@400;500;700&family=Arimo:wght@400;700&family=Itim&display=swap" rel="stylesheet">
<style>
:root{
  --navy:#0b3a66;
  --blue:#0f5a98;
  --blue-hi:#1a78bd;
  --cyan:#1aa8e2;
  --tile:#a9e3f8;
  --link:#1f79c4;
  --green:#7cb500;
  --ink:#222;
  --grey:#666;
  --page:#f2f2f2;
  --orange:#f05a14;
}
*{box-sizing:border-box;margin:0;padding:0}
html,body{width:800px;height:1200px;overflow:hidden}
body{position:relative;background:linear-gradient(#fff 0,var(--page) 180px);font-family:Ubuntu,sans-serif;color:var(--ink)}
.abs{position:absolute}

/* top bar */
.user-bar{left:529px;top:0;width:260px;height:32px;background:var(--navy);border-radius:0 0 4px 4px;display:flex;align-items:center;padding:0 8px 0 16px;gap:6px;font-family:Arimo,sans-serif;font-size:10px;color:#fff}
.flag{width:11px;height:8px;border:1px solid #fff}
.welcome{margin-left:16px}
.welcome b{font-family:Ubuntu,sans-serif;font-weight:400;font-size:14px;margin-left:3px}
.logout{margin-left:auto;background:var(--blue-hi);border-radius:4px;padding:4px 18px;font-size:10px}

/* brand */
.brand{left:14px;top:34px;width:180px;height:130px}
.brand-mark{position:absolute;left:40px;top:0;width:100px;height:100px;border-radius:50%;background:var(--navy)}
.brand-name{position:absolute;left:0;top:104px;width:180px;text-align:center;font-size:17px;font-weight:500;color:var(--navy);letter-spacing:1px}

/* search */
.search{left:360px;top:44px;width:430px;height:34px;background:var(--blue);padding:5px 6px;display:flex;gap:4px;font-family:Arimo,sans-serif;font-size:10px;color:#999}
.field{background:#fff;height:22px;display:flex;align-items:center;padding:0 6px}
.field.what{width:158px;justify-content:space-between}
.field.where{flex:1}
.go{width:18px;height:22px;background:var(--blue-hi);color:#fff;display:flex;align-items:center;justify-content:center;font-size:9px}

/* nav */
.main-nav{left:208px;top:92px;width:582px;height:39px;background:var(--blue);display:flex;font-family:Itim,cursive;font-size:15px;color:#fff}
.main-nav a{color:#fff;text-decoration:none;display:flex;align-items:center;padding:0 13px;margin-right:13px}
.main-nav a.active{background:var(--blue-hi)}
.nav-notch{right:10px;top:92px;width:0;height:0;border-top:19.5px solid transparent;border-bottom:19.5px solid transparent;border-right:26px solid #fff}

/* hero */
.hero{left:17px;top:173px;width:769px;height:222px;border-radius:5px;overflow:hidden;background:radial-gradient(circle at 62% 50%,#cfe4f3 0,#5f93bd 22%,#1b4f80 45%,#0c2f55 75%),#0c2f55}
.hero-list{position:absolute;left:0;top:26px;list-style:none}
.hero-list li{height:32.5px;display:flex;align-items:center;padding:0 14px 0 12px;font-size:17.5px;color:#fff;background:linear-gradient(90deg,rgba(10,30,55,.7),rgba(10,30,55,.35) 70%,transparent)}
.hero-list li::before{content:"";width:8px;height:8px;background:#fff;transform:rotate(45deg);margin-right:11px}

/* toolbox */
.toolbox{left:12px;top:408px;width:200px;height:376px}
.tool{position:absolute;left:32px;width:151px;height:34px;background:var(--tile);display:flex;align-items:center;gap:12px;padding-left:12px;font-size:12px;font-weight:500;color:var(--blue)}
.tool svg{width:24px;height:24px}
.join{position:absolute;left:24px;top:244px;width:134px;height:46px;border-radius:8px;background:linear-gradient(#ff8a2a,var(--orange) 60%,#d23c05);color:#fff;font-family:Ubuntu,sans-serif;font-weight:700;font-size:23px;display:flex;align-items:center;justify-content:center;letter-spacing:-.5px}

/* profile */
.profile{left:230px;top:427px;width:302px;height:325px}
.frame{position:absolute;inset:0}
.avatar{position:absolute;left:27px;top:23px;width:58px;height:68px;background:linear-gradient(#6a4e45,#3a2525 60%,#a83040)}
.profile-name{position:absolute;left:100px;top:17px;font-size:16px;font-weight:500;color:#333}
.facts{position:absolute;left:100px;top:49px;list-style:none;font-size:12px;color:#333}
.facts li{height:29.5px}
.facts span{color:var(--link)}
.profile-rule{position:absolute;left:6px;right:8px;top:282px;border-top:1px solid #ccc}
.edit{position:absolute;left:98px;top:292px;font-size:12px;color:var(--link);display:flex;gap:6px;align-items:center}

/* messages */
.messages{left:548px;top:424px;width:238px;height:328px}
.messages h2{position:absolute;left:20px;top:12px;font-size:14px;font-weight:700;color:var(--blue)}
.msg{position:absolute;left:20px;width:205px;font-size:9.8px;line-height:13.5px;color:#222}
.msg b{font-weight:500}
.msg a{color:var(--link)}
.msg-rule{position:absolute;left:8px;right:12px;border-top:1px solid #bbb}

/* calendar */
.calendar{left:18px;top:805px;width:768px;height:275px;background:#fff;border-radius:6px;overflow:hidden;font-family:Arimo,sans-serif;font-size:10.5px;color:#222}
.create{position:absolute;left:35px;top:12px;width:92px;height:22px;background:#d0301f;color:#fff;font-size:8.5px;font-weight:700;display:flex;align-items:center;padding-left:13px}
.create i{position:absolute;right:0;top:0;width:18px;height:22px;border-left:1px solid #f08070;display:flex;align-items:center;justify-content:center;font-style:normal}
.month{position:absolute;left:24px;top:54px;width:160px;display:flex;gap:5px;font-size:10.5px}
.month .pager{margin-left:auto;color:#777;display:flex;gap:10px}
.mini{position:absolute;left:35px;top:72px;border-collapse:collapse;font-size:9.6px;text-align:center}
.mini td{width:17.2px;height:15.2px;font-weight:700}
.mini tr:first-child td{font-weight:400}
.mini .dim{color:#999;font-weight:400}
.mini .today{outline:1px solid #333}
.cal-group{position:absolute;left:24px;font-size:10.5px;width:145px;display:flex;gap:6px}
.cal-group i{margin-left:auto;width:10px;height:9px;border:1px solid #aaa;font-style:normal}
.expand{position:absolute;left:170px;top:18px;font-size:11px;color:var(--link);display:flex;gap:10px}
.day{position:absolute;left:164px;width:604px;background:#fff}
.day.first{top:37px;height:104px;background:#eef3f9;border-bottom:1px solid #ccc}
.day.second{top:141px;height:134px}
.day-label{position:absolute;left:26px;top:7px;font-size:11px;color:var(--blue)}
.events{position:absolute;left:98px;top:5px;list-style:none}
.events li{height:18.4px;display:flex;align-items:center}
.events .arrow{width:12px;color:#555;font-size:10px}
.events .time{width:126px;margin-left:10px}
.events .who{color:var(--green);font-weight:700;font-size:10.5px}
.events .who::before{content:"⊞ ";color:#777;font-weight:400;font-size:8px}
.events .who::after{content:" ▢ ▲";color:#333;font-size:7px;font-weight:400}

/* footer */
.footer-nav{left:15px;top:1103px;width:771px;height:35px;background:linear-gradient(#fff,#eaeaea);display:flex;align-items:center;font-family:Arimo,sans-serif;font-size:11.5px;color:#333;padding-left:98px;gap:0}
.footer-nav a{color:#333;text-decoration:none;margin-right:40px}
.rights{left:20px;top:1148px;font-family:Arimo,sans-serif;font-size:9.5px;color:#444}
.connect{left:678px;top:1143px;font-family:Arimo,sans-serif;font-size:7.5px;color:#222}
.socials{left:677px;top:1157px;display:flex;gap:5px}
.social{width:31px;height:31px;border-radius:4px;display:flex;align-items:center;justify-content:center;font-family:Ubuntu,sans-serif;font-size:6.5px;color:#fff;background:var(--blue)}
</style>
</head>
<body>

<div class="abs user-bar">
  <span class="flag" style="background:#2a3f8f"></span>
  <span class="flag" style="background:#c33"></span>
  <span class="flag" style="background:#3a9a3a"></span>
  <span class="flag" style="background:#d82020"></span>
  <span class="welcome">Welcome<b>Jhon</b></span>
  <span class="logout">Logout</span>
</div>

<div class="abs brand">
  <span class="brand-mark"></span>
  <span class="brand-name">QuellNest</span>
</div>

<form class="abs search">
  <div class="field what">What <span style="color:#333">▼</span></div>
  <div class="field where">Search</div>
  <div class="go">GO</div>
</form>

<nav class="abs main-nav">
  <a class="active" href="#">Home</a>
  <a href="#">Features</a>
  <a href="#">How it works</a>
  <a href="#">Pricing</a>
  <a href="#">Contact us</a>
  <a href="#">FAQ</a>
</nav>
<div class="abs nav-notch"></div>

<section class="abs hero" role="img" aria-label="Blue digital globe with a wall clock, representing round-the-clock reservations">
  <ul class="hero-list">
    <li>Accpt 24/7 reservations</li>
    <li>Never reveal your schedule</li>
    <li>Automatic reminders</li>
    <li>Marketing Campaigns</li>
    <li>The more you quell, the more you save</li>
  </ul>
</section>

<aside class="abs toolbox">
  <svg class="frame" viewBox="0 0 200 376" width="200" height="376">
    <polygon points="96,4 108,2 106,34 196,28 198,332 110,334 112,372 92,374 90,328 2,322 0,32 96,34" fill="var(--navy)"/>
    <polygon points="102,14 100,44 188,40 190,322 102,322 104,362 98,364 96,316 10,312 12,44 96,46 96,16" fill="#0f6fa3"/>
    <polygon points="20,52 186,48 186,318 14,306" fill="var(--cyan)"/>
  </svg>
  <div class="tool" style="top:47px"><svg viewBox="0 0 24 24"><circle cx="12" cy="7" r="5" fill="#1a8fd6"/><path d="M2 23c0-7 4-10 10-10s10 3 10 10z" fill="#1a8fd6"/></svg>My Profile</div>
  <div class="tool" style="top:89px"><svg viewBox="0 0 24 24"><circle cx="10" cy="10" r="7" fill="none" stroke="#1a8fd6" stroke-width="3"/><path d="M15 15l7 7" stroke="#345" stroke-width="4"/></svg>MyNest</div>
  <div class="tool" style="top:131px"><svg viewBox="0 0 24 24"><ellipse cx="12" cy="10" rx="11" ry="8" fill="#1a8fd6"/><path d="M6 16l-2 6 7-5z" fill="#1a8fd6"/><path d="M6 8h12M6 11h12" stroke="#fff"/></svg>My Favorites</div>
  <div class="tool" style="top:173px"><svg viewBox="0 0 24 24"><circle cx="12" cy="12" r="8" fill="none" stroke="#1a8fd6" stroke-width="5" stroke-dasharray="3 2"/><circle cx="12" cy="12" r="4" fill="#1a8fd6"/></svg>Settings</div>
  <div class="join">JOIN NOW</div>
</aside>

<section class="abs profile">
  <svg class="frame" viewBox="0 0 302 325" width="302" height="325">
    <path d="M4 6 L300 2 L297 323 L2 318 Z" fill="#fff" stroke="#111" stroke-width="5"/>
  </svg>
  <div class="avatar" role="img" aria-label="Member profile photo"></div>
  <h1 class="profile-name">Ravin Kolhe</h1>
  <ul class="facts">
    <li><span>Working at:</span> Orbit Works</li>
    <li><span>Studied at:</span> Westfield university</li>
    <li><span>Lives :</span> Noida, India</li>
    <li><span>Language:</span> Hindi, English</li>
    <li><span>Location:</span> Jaipur, Rajasthan</li>
    <li><span>Born :</span> September 24</li>
    <li><span>Hobbies:</span> Cricket, Movies</li>
    <li><span>Status:</span> Married</li>
  </ul>
  <div class="profile-rule"></div>
  <div class="edit"><svg width="14" height="14" viewBox="0 0 14 14"><rect x="1" y="2" width="10" height="11" fill="#fff" stroke="#888"/><path d="M4 11l8-8" stroke="#d08000" stroke-width="2"/></svg>Edit Profile</div>
</section>

<section class="abs messages">
  <svg class="frame" viewBox="0 0 238 328" width="238" height="328">
    <path d="M3 6 L235 2 L233 326 L4 322 Z" fill="#fff" stroke="#111" stroke-width="5"/>
  </svg>
  <h2>Latest Messages</h2>
  <p class="msg" style="top:40px"><b>Devansh Mehra</b> ite dino bad like...kuch GADBAD lag raha h ....<br>about an hour ago · Like<br>Tarun Bhatt Kya baat h Nikhil g........ Raaaaapcheeeeek lag rahe ho...<br>about an hour ago · <a>Like</a></p>
  <div class="msg-rule" style="top:126px"></div>
  <p class="msg" style="top:133px"><b>Devansh Mehra</b> ite dino bad like...kuch GADBAD lag raha h ....<br>about an hour ago · Like<br>Tarun Bhatt Kya baat h Nikhil g........ Raaaaapcheeeeek lag rahe ho...<br>about an hour ago · <a>Like</a></p>
  <div class="msg-rule" style="top:222px"></div>
  <p class="msg" style="top:229px;left:19px"><b>Devansh Mehra</b> ite dino bad like...kuch GADBAD lag raha h ....<br>about an hour ago · Like<br>Tarun Bhatt Kya baat h Nikhil g........ Raaaaapcheeeeek lag rahe ho...<br>about an hour ago · <a>Like</a></p>
</section>

<section class="abs calendar">
  <div class="create">CREATE<i>▼</i></div>
  <div class="month"><span>▾</span>December 2011<span class="pager"><span>‹</span><span>›</span></span></div>
  <table class="mini">
    <tr><td>S</td><td>M</td><td>T</td><td>W</td><td>T</td><td>F</td><td>S</td></tr>
    <tr><td class="dim">27</td><td class="dim">28</td><td class="dim">29</td><td class="dim">30</td><td>1</td><td>2</td><td>3</td></tr>
    <tr><td>4</td><td>5</td><td>6</td><td>7</td><td>8</td><td>9</td><td>10</td></tr>
    <tr><td>11</td><td>12</td><td>13</td><td>14</td><td>15</td><td>16</td><td>17</td></tr>
    <tr><td>18</td><td>19</td><td>20</td><td>21</td><td class="today">22</td><td>23</td><td>24</td></tr>
    <tr><td>25</td><td>26</td><td>27</td><td>28</td><td>29</td><td>30</td><td>31</td></tr>
    <tr><td class="dim">1</td><td class="dim">2</td><td class="dim">3</td><td class="dim">4</td><td class="dim">5</td><td class="dim">6</td><td class="dim">7</td></tr>
  </table>
  <div class="cal-group" style="top:197px">▸ My calendars<i></i></div>
  <div class="cal-group" style="top:224px">▸ Other calendars<i></i></div>
  <div class="expand"><span>Expand All</span><span>Collapse All</span></div>

  <div class="day first">
    <span class="day-label">Thu Dec 22</span>
    <ul class="events">
      <li><span class="arrow">↶</span><span class="time">7:30am – 8:30am</span><span class="who">adverta</span></li>
      <li><span class="arrow">↶</span><span class="time">12:00pm – 12:30pm</span><span class="who">adverta-calendar@brindlo.com</span></li>
      <li><span class="arrow">↶</span><span class="time">1:30pm – 2:30pm</span><span class="who">adverta-calendar@brindlo.com</span></li>
      <li><span class="arrow">↶</span><span class="time">2:30pm – 3:30pm</span><span class="who">adverta-calendar@brindlo.com</span></li>
      <li><span class="arrow">↶</span><span class="time">11:30pm – 12:30am</span><span class="who">adverta-calendar@brindlo.com</span></li>
    </ul>
  </div>
  <div class="day second">
    <span class="day-label">Fri Dec 23</span>
    <ul class="events">
      <li><span class="arrow">↶</span><span class="time">11:30pm – 12:30am</span><span class="who">adverta-calendar@brindlo.com</span></li>
      <li><span class="arrow">↶</span><span class="time">3:00am – 4:00am</span><span class="who">adverta-calendar@brindlo.com</span></li>
      <li><span class="arrow">↶</span><span class="time">3:00am – 4:00am</span><span class="who">adverta-calendar@brindlo.com</span></li>
      <li><span class="arrow">↶</span><span class="time">7:30am – 8:30am</span><span class="who">adverta</span></li>
      <li><span class="arrow">↶</span><span class="time">12:00pm – 12:30pm</span><span class="who">adverta-calendar@brindlo.com</span></li>
      <li><span class="arrow">↶</span><span class="time">1:30pm – 2:30pm</span><span class="who">adverta-calendar@brindlo.com</span></li>
      <li><span class="arrow">↶</span><span class="time">2:30pm – 3:30pm</span><span class="who">adverta-calendar@brindlo.com</span></li>
    </ul>
  </div>
</section>

<footer>
  <nav class="abs footer-nav">
    <a href="#">Home</a>
    <a href="#">Privacy</a>
    <a href="#">Getting started</a>
    <a href="#">How it works</a>
    <a href="#">Pricing</a>
    <a href="#">Contact us</a>
    <a href="#">FAQ</a>
  </nav>
  <p class="abs rights">All rights reversed @ quellnest.com</p>
  <p class="abs connect">Connect with us:</p>
  <div class="abs socials">
    <span class="social" style="background:#2aa0d8">vexnor</span>
    <span class="social" style="background:#2f5ea8">tumbrella</span>
    <span class="social" style="background:#1a4f96">mor tan</span>
  </div>
</footer>

</body>
</html>
```